Design a box for EV Charging Cables - Electric Cars

https://files.plomtrex.example/doc/7qRwLm2ZxNa9/view

We are looking to design a box to package our EV charging cables. This box needs to be 40cm x 40cm x 11cm.

It needs to include:
- Our logo
- Images of our products
- Accreditations

My websites are:
https://voltharbor.co.uk/
https://www.plugmerrow.co.uk/
https://www.zandrel-amp.co.uk/

Logo:
https://pixdrop.example/Kq8Tz2L
https://pixdrop.example/Rw4Hn9B
https://pixdrop.example/Jd7Pv3X
https://pixdrop.example/Ny6Qb5G

Rather than having a list of products. I would like to have tick boxes:
1st tick box: Connector Type From: (Type 2, 3 Pin),
2nd tick box: Connector Type To: (Type 1, Type 2),
3rd tick box: Amp/Charge Speed (13amp/16amp/32amp/32amp - 3 Phase)
4th tick box: Length (5m/10m/15m)

Target Market(s)

People who own electric cars

Industry/Entity Type

Automotive

Colors

Designer to choose colors to be used in the design.

Requirements
Must have
• Our colours, logo, list of products we sell
Nice to have
• Rather than having a list of products. I would like to have tick boxes: 1st tick box should be: Connector Type From: (Type 2, 3 Pin), Connector Type To: (Type 1, Type 2), Third: Amp/Charge Speed (13amp/16amp/32amp/32amp - 3 Phase) Third: Length (5m/10m/15m)
Should not have
• Transparent Section

```html
<!DOCTYPE html>
<html lang="en">
<head>
<meta charset="utf-8">
<title>Zandrel Charging Cable Box</title>
<link rel="stylesheet" href="https://fonts.googleapis.com/css2?family=Exo+2:wght@300;400;500;600&display=swap">
<style>
  :root {
    --stage: #86977c;
    --box-black: #141414;
    --box-charcoal: #1f1f1f;
    --green-deep: #138a3f;
    --green-mid: #3fae48;
    --green-bright: #6cc24a;
    --green-lime: #a6d63c;
    --ink-white: #f4f4f2;
    --label-white: #ffffff;
    --label-ink: #222222;
    --photo-dark: #2a2f2b;
  }
  html, body {
    margin: 0;
    padding: 0;
    width: 1200px;
    height: 2818px;
    overflow: hidden;
    background: var(--stage);
  }
  .artboard {
    display: block;
    width: 1200px;
    height: 2818px;
    font-family: "Exo 2", sans-serif;
  }
  .panel-bg { fill: var(--box-black); }
  .flap { fill: var(--box-black); }
  .band-bright { fill: var(--green-bright); }
  .band-deep { fill: var(--green-deep); }
  .band-mid { fill: var(--green-mid); }
  .brand-name { fill: var(--green-lime); font-weight: 600; letter-spacing: 1px; }
  .product-title { fill: var(--ink-white); font-weight: 400; letter-spacing: 1px; }
  .level-tag { fill: none; stroke: var(--ink-white); stroke-width: 0.8; }
  .level-text { fill: var(--ink-white); font-weight: 300; font-style: normal; }
  .web-address { fill: var(--ink-white); font-weight: 300; letter-spacing: 2px; }
  .tick-box { fill: var(--label-white); }
  .spec-text { fill: var(--ink-white); font-weight: 400; }
  .spec-label { fill: var(--label-white); }
  .spec-label-head { fill: var(--label-ink); }
  .spec-label-head-text { fill: var(--label-white); font-weight: 600; letter-spacing: 1px; }
  .spec-label-text { fill: var(--label-ink); font-weight: 400; }
  .cert-mark { fill: var(--ink-white); }
</style>
</head>
<body>
<svg class="artboard" viewBox="0 0 1200 2818" xmlns="http://www.w3.org/2000/svg" xmlns:xlink="http://www.w3.org/1999/xlink">
  <defs>
    <linearGradient id="band-gradient" x1="0" y1="1" x2="1" y2="0">
      <stop offset="0" stop-color="#1a9a46"/>
      <stop offset="1" stop-color="#5dbb49"/>
    </linearGradient>
    <linearGradient id="black-sheen" x1="0" y1="0" x2="1" y2="1">
      <stop offset="0" stop-color="#222222"/>
      <stop offset="1" stop-color="#0d0d0d"/>
    </linearGradient>
    <linearGradient id="photo-tone" x1="0" y1="0" x2="1" y2="1">
      <stop offset="0" stop-color="#3a3f3b"/>
      <stop offset="0.6" stop-color="#1b1d1c"/>
      <stop offset="1" stop-color="#4f8f45"/>
    </linearGradient>

    <!-- Lid face: 40 x 40 -->
    <symbol id="lid-face" viewBox="0 0 400 400">
      <rect class="panel-bg" width="400" height="400" fill="url(#black-sheen)"/>
      <polygon class="band-bright" points="232,0 244,0 30,400 18,400"/>
      <polygon points="262,0 400,0 400,150 200,400 58,400" fill="url(#band-gradient)"/>
      <polygon class="band-deep" points="290,0 304,0 92,400 78,400"/>
      <polygon class="band-bright" points="300,110 362,110 232,272 170,272"/>
      <polygon class="band-mid" points="400,130 400,200 300,330 258,330"/>
      <polygon class="band-bright" points="380,40 400,40 400,70 356,70"/>
      <text class="brand-name" x="40" y="68" font-size="40">ZANDREL</text>
      <text class="product-title" x="40" y="125" font-size="36">CHARGING</text>
      <text class="product-title" x="40" y="167" font-size="36">CABLE</text>
      <rect class="level-tag" x="152" y="148" width="68" height="19"/>
      <text class="level-text" x="186" y="162" font-size="12" text-anchor="middle">LEVEL 2</text>
      <g role="img" aria-label="Product photo: coiled black charging cable with green-trimmed Type 2 connector, mains plug and control box">
        <rect x="14" y="190" width="270" height="190" rx="14" fill="url(#photo-tone)"/>
      </g>
      <text class="web-address" x="385" y="388" font-size="9" text-anchor="end">www.voltharbor.co.uk</text>
    </symbol>

    <!-- Side panel with tick boxes: 40 x 11 -->
    <symbol id="side-spec" viewBox="0 0 400 110">
      <rect class="panel-bg" width="400" height="110" fill="url(#black-sheen)"/>
      <polygon points="0,0 150,0 112,110 0,110" fill="url(#band-gradient)"/>
      <polygon class="band-bright" points="158,0 166,0 128,110 120,110"/>
      <text class="brand-name" x="14" y="38" font-size="18">ZANDREL</text>
      <text class="product-title" x="14" y="60" font-size="13">CHARGING</text>
      <text class="product-title" x="14" y="76" font-size="13">CABLE</text>
      <rect class="tick-box" x="170" y="28" width="10" height="10"/>
      <text class="spec-text" x="186" y="34" font-size="7">Connector Type From:</text>
      <text class="spec-text" x="186" y="43" font-size="7">(Type 2, 3 Pin)</text>
      <rect class="tick-box" x="170" y="64" width="10" height="10"/>
      <text class="spec-text" x="186" y="70" font-size="7">Length:</text>
      <text class="spec-text" x="186" y="79" font-size="7">(5m/10m/15m)</text>
      <rect class="tick-box" x="268" y="28" width="10" height="10"/>
      <text class="spec-text" x="284" y="34" font-size="7">Connector Type To:</text>
      <text class="spec-text" x="284" y="43" font-size="7">(Type 1, Type 2)</text>
      <rect class="tick-box" x="268" y="64" width="10" height="10"/>
      <text class="spec-text" x="284" y="70" font-size="7">Amp/Charge Speed:</text>
      <text class="spec-text" x="284" y="79" font-size="6.2">(13amp/16amp/32amp/32amp - 3 Phase)</text>
    </symbol>

    <!-- Side panel with specification label and certification marks: 40 x 11 -->
    <symbol id="side-label" viewBox="0 0 400 110">
      <rect class="panel-bg" width="400" height="110" fill="url(#black-sheen)"/>
      <polygon points="0,0 70,0 32,110 0,110" fill="url(#band-gradient)"/>
      <polygon class="band-bright" points="78,0 86,0 48,110 40,110"/>
      <rect class="spec-label" x="100" y="18" width="150" height="74" rx="8"/>
      <rect class="spec-label-head" x="110" y="26" width="130" height="12"/>
      <text class="spec-label-head-text" x="175" y="35" font-size="7" text-anchor="middle">SPECIFICATION</text>
      <text class="spec-label-text" x="112" y="49" font-size="7">Model: Portable EV Charger</text>
      <text class="spec-label-text" x="112" y="60" font-size="7">Input: 230V AC 50Hz</text>
      <text class="spec-label-text" x="112" y="71" font-size="7">Output: 16A Max</text>
      <text class="spec-label-text" x="112" y="82" font-size="7">Cable: 5m Type 2</text>
      <rect class="cert-mark" x="290" y="44" width="18" height="18" rx="4"/>
      <rect class="cert-mark" x="316" y="44" width="18" height="18" rx="4"/>
      <polygon class="cert-mark" points="351,44 361,62 341,62"/>
      <text class="web-address" x="385" y="100" font-size="7" text-anchor="end">www.voltharbor.co.uk</text>
    </symbol>

    <!-- Plain end panel -->
    <symbol id="side-plain" viewBox="0 0 400 110">
      <rect class="panel-bg" width="400" height="110" fill="url(#black-sheen)"/>
      <text class="brand-name" x="200" y="66" font-size="22" text-anchor="middle">ZANDREL</text>
    </symbol>
  </defs>

  <!-- Lid artwork -->
  <g class="lid-view">
    <use xlink:href="#lid-face" href="#lid-face" x="300" y="200" width="600" height="600"/>
  </g>

  <!-- Flat dieline -->
  <g class="dieline" transform="translate(0,1000)">
    <!-- base face -->
    <use href="#lid-face" x="218" y="300" width="300" height="300"/>
    <!-- spec side (vertical) -->
    <use href="#side-spec" width="300" height="82.5" transform="translate(600.5,300) rotate(90)"/>
    <!-- lid face -->
    <use href="#lid-face" x="600.5" y="300" width="300" height="300"/>
    <!-- label side (vertical) -->
    <use href="#side-label" width="300" height="82.5" transform="translate(983,300) rotate(90)"/>
    <!-- end panels -->
    <use href="#side-plain" x="600.5" y="217.5" width="300" height="82.5"/>
    <use href="#side-plain" x="600.5" y="600" width="300" height="82.5"/>
    <use href="#side-plain" x="218" y="217.5" width="300" height="82.5"/>
    <use href="#side-plain" x="218" y="600" width="300" height="82.5"/>
    <!-- tuck flaps -->
    <path class="flap" d="M218,217.5 L218,170 Q218,130 258,130 L478,130 Q518,130 518,170 L518,217.5 Z"/>
    <path class="flap" d="M218,682.5 L218,730 Q218,770 258,770 L478,770 Q518,770 518,730 L518,682.5 Z"/>
    <path class="flap" d="M983,300 L1050,318 L1050,582 L983,600 Z"/>
    <path class="flap" d="M218,300 L160,318 L160,582 L218,600 Z"/>
    <path class="flap" d="M900.5,217.5 L960,235 L960,282 L900.5,300 Z"/>
    <path class="flap" d="M900.5,600 L960,618 L960,665 L900.5,682.5 Z"/>
  </g>

  <!-- Side panels at print size -->
  <g class="side-panels">
    <use href="#side-spec" x="80" y="2030" width="1040" height="286"/>
    <use href="#side-label" x="80" y="2420" width="1040" height="286"/>
  </g>
</svg>
</body>
</html>
```